I am a surgeon that operates on gynaecological cancer. Wish a design and logo for letter head.

Design should include my name: Dr. Kiran Mudaly, qualifications: FTELSWOB, CGO. and state that I am a Gynaecological Oncologist and Advanced Laparoscopic Surgeon.
As for a logo. As all cancer is related to DNA, I think that that double helix could be used to symbolise a female shape, exaggerating the abdomen to suggest a mass.

Reason: Extended to view changes I have asked for.

```html
<!DOCTYPE html>
<html lang="en">
<head>
<meta charset="utf-8">
<title>Dr. Kiran Mudaly – Letterhead</title>
<link rel="stylesheet" href="https://fonts.googleapis.com/css2?family=Arimo:wght@400;700&family=Open+Sans:wght@400&family=Pinyon+Script&display=swap">
<style>
  :root {
    --brand-blue: #1f5fa8;
    --band-blue: #2f8ff0;
    --band-orange: #fb9b13;
    --ink: #2e2e2e;
    --ink-soft: #5a5a5a;
    --paper: #ffffff;
  }
  * { box-sizing: border-box; margin: 0; padding: 0; }
  html, body { width: 928px; height: 1200px; overflow: hidden; background: var(--paper); }
  .letterhead {
    position: relative;
    width: 928px;
    height: 1200px;
    background: var(--paper);
    font-family: "Arimo", Arial, sans-serif;
    color: var(--ink);
  }
  .brand {
    position: absolute;
    left: 42px;
    top: 36px;
    display: flex;
    align-items: flex-start;
    gap: 14px;
  }
  .brand-dot {
    width: 26px;
    height: 26px;
    margin-top: 12px;
    border-radius: 50%;
    background: var(--band-orange);
  }
  .brand-name {
    font-family: "Open Sans", Arial, sans-serif;
    font-weight: 400;
    font-size: 36px;
    line-height: 40px;
    color: var(--brand-blue);
  }
  .practitioner {
    position: absolute;
    left: 694px;
    top: 30px;
    color: var(--ink-soft);
  }
  .practitioner-name { font-size: 17px; line-height: 22px; }
  .practitioner-quals {
    font-size: 10.5px;
    line-height: 14px;
    padding-left: 76px;
    letter-spacing: 0.2px;
  }
  .practitioner-role { font-size: 13px; line-height: 16px; margin-top: 4px; }
  .salutation {
    position: absolute;
    left: 84px;
    top: 233px;
    font-size: 16.5px;
  }
  .letter-body {
    position: absolute;
    left: 155px;
    top: 270px;
    width: 706px;
  }
  .letter-body p {
    font-size: 16.3px;
    line-height: 20.5px;
    margin-bottom: 21px;
  }
  .signature {
    position: absolute;
    left: 78px;
    top: 895px;
    font-family: "Pinyon Script", cursive;
    font-size: 50px;
    color: #222;
  }
  .footer-bands {
    position: absolute;
    left: 0;
    top: 1030px;
    width: 928px;
    height: 170px;
  }
  .footer-info {
    position: absolute;
    top: 1128px;
    color: #ffffff;
    font-size: 13px;
    line-height: 17px;
  }
  .footer-address { left: 77px; }
  .footer-phone { left: 348px; }
  .footer-web { left: 642px; text-align: right; }
  .footer-info b { font-weight: 700; }
</style>
</head>
<body>
<div class="letterhead">
  <header>
    <div class="brand">
      <span class="brand-dot"></span>
      <div class="brand-name">Dr. Kiran<br>Mudaly</div>
    </div>
    <div class="practitioner">
      <div class="practitioner-name">Dr. Kiran Mudaly</div>
      <div class="practitioner-quals">FTELSWOB, CGO.</div>
      <div class="practitioner-role">Gynaecological Oncologist and<br>Advanced Laparoscopic Surgeon.</div>
    </div>
  </header>

  <main>
    <p class="salutation">Dear Sir / Madam,</p>
    <div class="letter-body">
      <p>Lorem ipsum dolor sit amet, consectetur adipisicing elit, sed do eiusmod tempor labore et olore magna aliqua. Ut enim ad minim veniam, quis nostrud exercitation ullamco laboris nisi ut aliquip ex ea commodo consequa.Lorem ipsum dolor sit amet, nsectetur adipisicing elit, sed do eiusmod tempor incididunt ut labore et dolore magna aliqua. Ut enim ad minim veniam, quis.</p>
      <p>Lorem ipsum dolor sit amet, consectetur adipisicing elit, sed do eiusmod tempor labore et dolore magna aliqua. Ut enim ad minim veniam, quis nostrud exercitation ullamco laboris nisi ut aliquip ex ea commodo consequa.Lorem ipsum dolor sit amet, nsectetur adipisicing elit, sed do eiusmod tempor incididunt ut labore et dolore magna aliqua. Ut enim ad minim veniam, quis.</p>
      <p>Lorem ipsum dolor sit amet, consectetur adipisicing elit, sed do eiusmod tempor labore et dolore magna aliqua. Ut enim ad minim veniam, quis nostrud exercitation ullamco laboris nisi ut aliquip ex ea commodo consequa.Lorem ipsum dolor sit amet, nsectetur adipisicing elit, sed do eiusmod tempor incididunt ut labore et dolore magna aliqua. Ut enim ad minim veniam, quis.</p>
      <p>Lorem ipsum dolor sit amet, consectetur adipisicing elit, sed do eiusmod tempor labore et dolore magna aliqua. Ut enim ad minim veniam, quis nostrud exercitation ullamco laboris nisi ut aliquip ex ea commodo consequa.Lorem ipsum dolor sit amet, nsectetur adipisicing elit, sed do eiusmod tempor incididunt ut labore et dolore magna aliqua. Ut enim ad minim veniam, quis.</p>
      <p>Lorem ipsum dolor sit amet, consectetur adipisicing elit, sed do eiusmod tempor labore et dolore magna aliqua. Ut enim ad minim veniam, quis nostrud exercitation ullamco laboris nisi ut aliquip ex ea commodo consequa.Lorem ipsum dolor sit amet, nsectetur adipisicing elit, sed do eiusmod tempor incididunt ut labore et dolore magna aliqua. Ut enim ad minim veniam, quis.</p>
    </div>
    <p class="signature">Your Name</p>
  </main>

  <footer>
    <svg class="footer-bands" viewBox="0 0 928 170" aria-hidden="true">
      <path d="M0,14 Q420,120 928,42 L928,60 Q420,138 0,36 Z" fill="var(--band-blue)"/>
      <path d="M0,44 Q420,146 928,66 L928,170 L0,170 Z" fill="var(--band-orange)"/>
    </svg>
    <div class="footer-info footer-address">ABC<br>any street<br>Country</div>
    <div class="footer-info footer-phone"><b>Tel :</b> +000 000 0000<br><b>Mob :</b> +000 000 0000</div>
    <div class="footer-info footer-web"><b>E-mail :</b> name@kiranmudaly.com<br><b>Web :</b> www.drkiranmudaly.com</div>
  </footer>
</div>
</body>
</html>
```